Plakat-Design für eine Budgetplanung für ein Kinderbuch
Das vorgeschlagene Poster war von Anfang an unser Favorit. Es zeichnet sich aus, durch ein ansprechendes, klares und kindgerechtes Design. Wir haben die ausgesprochen zuverlässige Arbeit und Kommunikation sehr geschätzt und hoffen auf weitere Zusammenarbeit.
Zielgruppe
Wir sind ein Verlag und bringen nächsten Monat zwei Kinder-/Jugendbücher mit dem Thema Finanzbildung heraus. Das Alter der Zielgruppe ist zwischen 8 und 13 Jahren. Zu den Büchern gehört ein hochwertiges Posterset aus drei Postern. In diesem Auftrag soll zunächst das erste Poster designed werden. Hier geht es darum eine kleine 'Budgetplanung' zu erstellen. In weiteren Aufträgen sollen auch Illustrationen aufgewertet und Designs für Websites erstellt werden.
Aufgabenstellung
Wir werden einige Bilder bereitstellen, die verarbeitet werden dürfen (es müssen nicht alle verwendet werden!). Es wäre schön, wenn das Posterdesign so ausgelegt wird, dass die Bilder gut in das Gesamtdesign passen. Die Bildqualität des Posters soll auf DINA2 optimiert sein. Weiterhin stellen wir einen 'Beispiel-Geldplan' zur Verfügung, der alle Texte enthält, die das Poster beinhalten soll. Das Design dieses Beispiel-Geldplans soll unberücksichtigt bleiben. Das Gesamtdesign soll hochwertig und kreativ sein.

```html
<!DOCTYPE html>
<html lang="de">
<head>
<meta charset="utf-8">
<title>Wie ich mir meine Träume erfülle – Budgetplan</title>
<link rel="stylesheet" href="https://fonts.googleapis.com/css2?family=Bangers&family=Roboto:wght@300&display=swap">
<style>
  :root {
    --navy: #123a8c;
    --blue: #0a5a9a;
    --teal: #00a19a;
    --teal-deep: #007a80;
    --mint: #6dc19b;
    --plum: #8e2070;
    --night: #302c4c;
    --white: #ffffff;
    --paper: #ffffff;
  }
  * { box-sizing: border-box; margin: 0; padding: 0; }
  html, body { width: 1200px; height: 1200px; overflow: hidden; background: var(--paper); }
  .poster {
    position: absolute; left: 212px; top: 51px;
    width: 775px; height: 1097px; overflow: hidden;
    color: var(--white);
    font-family: "Roboto", Arial, sans-serif; font-weight: 300;
  }
  .band { position: absolute; left: 0; width: 775px; }
  .band--header { top: 0; height: 183px; background: linear-gradient(90deg, var(--navy) 0%, var(--blue) 35%, var(--teal) 100%); }
  .band--income { top: 183px; height: 183px; background: linear-gradient(90deg, var(--mint) 0%, var(--teal) 45%, var(--teal) 100%); }
  .band--needs { top: 366px; height: 183px; background: linear-gradient(90deg, var(--mint) 0%, var(--teal) 40%, #6a5a84 75%, var(--plum) 100%); }
  .band--goals { top: 549px; height: 183px; background: linear-gradient(90deg, var(--teal) 0%, var(--teal) 45%, #6a5a84 70%, var(--plum) 100%); }
  .band--saved { top: 732px; height: 183px; background: linear-gradient(90deg, var(--teal) 0%, var(--teal-deep) 45%, #1f4f63 70%, var(--night) 100%); }
  .band--dreams { top: 915px; height: 182px; background: linear-gradient(90deg, var(--mint) 0%, var(--teal) 30%, #1f5a6e 65%, var(--night) 100%); }

  .line { position: absolute; white-space: nowrap; line-height: 1; }
  .headline { font-family: "Bangers", "Impact", sans-serif; font-weight: 400; letter-spacing: 0.5px; font-size: 31px; }
  .label { font-size: 26px; }
  .title-lead { font-size: 28px; }
  .title-main { font-family: "Bangers", "Impact", sans-serif; font-size: 64px; letter-spacing: 1px; }
  .closing { font-family: "Bangers", "Impact", sans-serif; font-size: 49px; letter-spacing: 1px; }
  .right { right: 56px; text-align: right; }
  .field { position: absolute; width: 89px; height: 30px; background: var(--white); }
  .art { position: absolute; border-radius: 18px; }
</style>
</head>
<body>
<main class="poster">
  <section class="band band--header"></section>
  <section class="band band--income"></section>
  <section class="band band--needs"></section>
  <section class="band band--goals"></section>
  <section class="band band--saved"></section>
  <section class="band band--dreams"></section>

  <!-- Titel -->
  <span class="line title-lead" style="left:59px; top:90px;">Wie ich mir meine</span>
  <span class="line title-main" style="left:290px; top:64px;">TRÄUME ERFÜLLE</span>

  <!-- Einnahmen -->
  <span class="line headline" style="left:55px; top:196px;">ICH ERHALTE JEDEN MONAT:</span>
  <div class="field" style="left:420px; top:193px;"></div>
  <span class="line label" style="left:55px; top:242px;">Davon Taschengeld:</span>
  <div class="field" style="left:314px; top:237px;"></div>
  <span class="line label" style="left:55px; top:286px;">Aus meinem Verdienst:</span>
  <div class="field" style="left:350px; top:281px;"></div>
  <span class="line label" style="left:55px; top:330px;">Durch meine Investition:</span>
  <div class="field" style="left:366px; top:325px;"></div>
  <div class="art" role="img" aria-label="Illustration: Figur mit Glühbirnen rechnet an einer Tafel"
       style="left:530px; top:129px; width:169px; height:266px; background:linear-gradient(160deg,#f6e36a 0%,#8fc7ef 45%,#5aa3dd 100%); opacity:.85;"></div>

  <!-- Ausgaben -->
  <div class="art" role="img" aria-label="Illustration: grüner Geldschein mit Europakarte und Figuren"
       style="left:24px; top:386px; width:303px; height:145px; border-radius:4px; background:linear-gradient(90deg,#a6d6bd 0%,#9ccf8a 50%,#e9c640 75%,#a6d6bd 100%);"></div>
  <span class="line headline right" style="top:405px;">ICH BRAUCHE JEDEN MONAT</span>
  <span class="line label right" style="top:443px;">(für Freizeit, Essen etc.):</span>
  <div class="field" style="left:631px; top:477px;"></div>

  <!-- Ziele -->
  <span class="line headline" style="left:55px; top:580px;">ICH MÖCHTE SPAREN:</span>
  <div class="field" style="left:331px; top:579px;"></div>
  <span class="line headline" style="left:55px; top:624px;">ICH MÖCHTE INVESTIEREN:</span>
  <div class="field" style="left:394px; top:623px;"></div>
  <span class="line headline" style="left:55px; top:668px;">ICH MÖCHTE SPENDEN:</span>
  <div class="field" style="left:350px; top:667px;"></div>
  <div class="art" role="img" aria-label="Illustration: orange Figur hält ein großes Euro-Zeichen"
       style="left:520px; top:514px; width:166px; height:244px; background:linear-gradient(160deg,#f0f0f0 0%,#ef7d45 40%,#d9602a 100%); opacity:.85;"></div>

  <!-- Erspartes -->
  <div class="art" role="img" aria-label="Illustration: bunte Figuren reiten auf einem rosa Sparschwein und ziehen einen Wagen mit Münzen"
       style="left:24px; top:720px; width:291px; height:222px; background:linear-gradient(180deg,#c9d84a 0%,#d4639a 45%,#f3c3c8 75%,#f3c3c8 100%); opacity:.85;"></div>
  <span class="line headline right" style="top:774px;">WIE VIEL ICH SCHON</span>
  <span class="line headline right" style="top:808px;">GESPART HABE:</span>
  <div class="field" style="left:631px; top:846px;"></div>

  <!-- Abschluss -->
  <span class="line closing" style="left:55px; top:956px;">MEINE TRÄUME GEHEN</span>
  <span class="line closing" style="left:55px; top:1006px;">IN ERFÜLLUNG</span>
  <div class="art" role="img" aria-label="Illustration: Figuren baden fröhlich in einem Berg goldener Münzen"
       style="left:468px; top:971px; width:288px; height:110px; border-radius:50px; background:linear-gradient(90deg,#3a7fd0 0%,#f7e43a 20%,#f7e43a 80%,#d25aa0 100%); opacity:.9;"></div>
</main>
</body>
</html>
```